Cardiology practice business card

We need a business card for our cardiology practice "Bellmoor Cardiology". We have a new logo, attached below. We like the colours in the logo - red and charcoal. The front of the business card will need to have the doctors name, address, phone number and email. The back will need to have space to write 2 appointment dates and times.

```html
<!DOCTYPE html>
<html lang="en">
<head>
<meta charset="utf-8">
<title>Bellmoor Cardiology – Business Card</title>
<link rel="stylesheet" href="https://fonts.googleapis.com/css2?family=Lato:wght@400;700&family=Montserrat:wght@500;600&display=swap">
<style>
  :root {
    --red: #e0141b;
    --charcoal: #404145;
    --ink: #3a3a3d;
    --paper: #ffffff;
    --backdrop: #2b2c2f;
  }
  * { margin: 0; padding: 0; box-sizing: border-box; }
  html, body { width: 1200px; height: 952px; overflow: hidden; }
  body {
    background: var(--backdrop);
    font-family: "Lato", Arial, sans-serif;
    position: relative;
  }
  .card {
    position: absolute;
    width: 540px;
    height: 310px;
    background: var(--paper);
    overflow: hidden;
    box-shadow: 0 14px 30px rgba(0,0,0,.45);
  }

  /* Front */
  .card--front { left: 610px; top: 120px; }
  .front__tab {
    position: absolute; left: -20px; top: 30px;
    width: 150px; height: 110px;
    background: var(--charcoal); border-radius: 10px;
  }
  .front__rule {
    position: absolute; left: 170px; right: 0; top: 188px;
    height: 4px; background: var(--charcoal);
  }
  .front__details {
    position: absolute; left: 200px; top: 70px; right: 30px;
    color: var(--ink);
  }
  .doctor-name {
    font-weight: 700; font-size: 27px; color: var(--red);
    letter-spacing: .3px;
  }
  .doctor-role { font-size: 14px; margin: 2px 0 12px 20px; }
  .contact-row {
    display: flex; gap: 18px; font-size: 13px; align-items: center;
  }
  .contact-row svg { width: 12px; height: 12px; fill: var(--red); margin-right: 5px; vertical-align: -1px; }
  .front__address {
    position: absolute; left: 200px; top: 205px; right: 30px;
    font-size: 13px; color: var(--ink); line-height: 1.6;
  }
  .front__address .web { color: var(--red); }

  /* Back */
  .card--back { left: 60px; top: 500px; }
  .back__tab {
    position: absolute; width: 130px; height: 80px;
    background: var(--charcoal); border-radius: 12px;
  }
  .back__tab--top { left: -40px; top: -30px; }
  .back__tab--bottom { right: -40px; bottom: -30px; }
  .wordmark {
    position: absolute; left: 0; right: 0; top: 70px;
    display: flex; justify-content: center; align-items: center; gap: 10px;
    font-family: "Montserrat", Arial, sans-serif; font-weight: 600;
    font-size: 26px; color: var(--red); letter-spacing: 1.5px; text-transform: uppercase;
  }
  .wordmark__dot { width: 14px; height: 14px; border-radius: 50%; background: var(--red); }
  .appointments {
    position: absolute; left: 60px; right: 70px; top: 160px;
    font-family: "Montserrat", Arial, sans-serif;
  }
  .appointment-line {
    display: flex; align-items: flex-end; gap: 8px;
    color: var(--red); font-size: 15px; font-weight: 500;
    margin-bottom: 26px;
  }
  .appointment-line .blank {
    flex: 1; border-bottom: 2px dotted #8a8a8e; height: 1px; margin-bottom: 4px;
  }
</style>
</head>
<body>

  <section class="card card--front" aria-label="Business card front">
    <div class="front__tab"></div>
    <div class="front__rule"></div>
    <div class="front__details">
      <h1 class="doctor-name">Dr.Helen Marsden</h1>
      <p class="doctor-role">Managing Director</p>
      <div class="contact-row">
        <span><svg viewBox="0 0 24 24"><path d="M6.6 10.8a15.1 15.1 0 0 0 6.6 6.6l2.2-2.2a1 1 0 0 1 1-.25 11.4 11.4 0 0 0 3.6.6 1 1 0 0 1 1 1V20a1 1 0 0 1-1 1A17 17 0 0 1 3 4a1 1 0 0 1 1-1h3.5a1 1 0 0 1 1 1c0 1.25.2 2.45.6 3.6a1 1 0 0 1-.25 1z"/></svg>+00 987 654 32</span>
        <span><svg viewBox="0 0 24 24"><path d="M2 5h20v14H2z M2 5l10 8 10-8" fill="var(--red)"/></svg>hello@bellmoorheart.com</span>
      </div>
    </div>
    <div class="front__address">
      <p>2170 Harbor Lane Riverton, DC 20031</p>
      <p>www.<span class="web">bellmoorheart</span>.com</p>
    </div>
  </section>

  <section class="card card--back" aria-label="Business card back">
    <div class="back__tab back__tab--top"></div>
    <div class="back__tab back__tab--bottom"></div>
    <div class="wordmark"><span class="wordmark__dot"></span>Bellmoor Cardiology</div>
    <div class="appointments">
      <div class="appointment-line"><span>Date :</span><span class="blank"></span></div>
      <div class="appointment-line"><span>Time :</span><span class="blank"></span></div>
    </div>
  </section>

</body>
</html>
```